Webdesign für Umwelt- und Vertriebsmanagement
Zielgruppe
- Umwelt- und Vertriebsmanagement
- Erarbeitung von Konzepten und Lösungen für Recyclingunternehmen
Aufgabenstellung
keine Googlemaps-Karte in das Mockup
Navigation:
- Home
- Leistungen
- Beratung
- Vertrieb
- Recycling
- Zertifikate
- Vorstellung
- Partner
- Aktuelles
- Kontakt
- Impressum / Datenschutz
in den content vorrangig die Leistungen und den Kontakt darstellen
NUR FOTOS VON 'PIXANTO' NUTZEN!

```html
<!DOCTYPE html>
<html lang="de">
<head>
<meta charset="utf-8">
<title>Grünwerk – Beratung, Vertrieb, Recycling</title>
<link href="https://fonts.googleapis.com/css2?family=Ubuntu:wght@400;500;700&family=Roboto:ital,wght@0,300;0,400;0,500;1,400&family=Montserrat:wght@500;600&family=Poppins:wght@400;500&display=swap" rel="stylesheet">
<style>
:root{
  --green:#73a043;
  --green-dark:#5f8a34;
  --dark:#333333;
  --text:#3a3a3a;
  --muted:#555;
  --gray-bg:#f1f3f2;
  --pale:#f8faf2;
  --white:#fff;
}
*{box-sizing:border-box;margin:0;padding:0}
html,body{width:1200px;height:2835px;overflow:hidden}
body{position:relative;background:var(--white);font-family:Roboto,sans-serif;color:var(--text)}
.abs{position:absolute}

/* header */
.header{top:0;left:0;width:1200px;height:89px;background:var(--white)}
.brand{display:flex;align-items:center;gap:10px;position:absolute}
.brand-mark{width:22px;height:22px;background:var(--green)}
.brand-name{font-family:Ubuntu,sans-serif;font-weight:500;font-size:34px;color:var(--green);line-height:40px}
.header .brand{left:98px;top:20px}
.phone{position:absolute;left:825px;top:26px;font-family:Roboto,sans-serif;font-size:14px;color:var(--green);display:flex;align-items:center;gap:8px}
.btn-contact{position:absolute;left:983px;top:22px;width:119px;height:32px;background:var(--green);color:#fff;font-family:Ubuntu,sans-serif;font-size:16px;display:flex;align-items:center;justify-content:center}

/* nav */
.nav{top:89px;left:0;width:1200px;height:51px;background:var(--green)}
.nav ul{list-style:none;display:flex;position:absolute;left:98px;top:0;height:51px}
.nav li{font-family:Ubuntu,sans-serif;font-weight:500;font-size:15px;color:#fff;display:flex;align-items:center;padding:0 12px}
.nav li.active{background:var(--dark);padding:0 10px}
.nav li:nth-child(n+5){font-size:16px;padding:0 14px}

/* hero */
.hero{top:140px;left:0;width:1200px;height:600px;background:linear-gradient(180deg,#8c9aa6 0%,#c9a37a 30%,#f0b45a 52%,#f7c46b 60%,#b98a3c 72%,#6f7a35 82%,#4f6a2c 100%)}
.hero-title{position:absolute;top:262px;width:1200px;text-align:center;font-family:Montserrat,sans-serif;font-weight:600;font-size:33px;letter-spacing:5px;color:#1d1d1d}
.hero-sub{position:absolute;top:310px;width:1200px;text-align:center;font-family:Montserrat,sans-serif;font-weight:500;font-size:11.5px;letter-spacing:3px;color:#1d1d1d}
.hero-arrow{position:absolute;top:275px}

/* intro cards */
.intro{top:740px;left:0;width:1200px;height:596px;background:var(--gray-bg)}
.card{position:absolute;color:#fff;padding:26px 22px}
.card.dark{background:var(--dark);top:100px;height:382px}
.card.green{background:var(--green);top:76px;height:428px;padding-top:50px}
.card h2{font-family:Ubuntu,sans-serif;font-weight:400;font-size:31px;line-height:36px}
.card .lead{font-size:13px;margin-top:8px}
.card p{font-size:13px;line-height:18.5px;margin-top:10px}
.card .body{margin-top:30px}
.card .btn{position:absolute;left:23px;width:158px;height:47px;background:#fff;color:#222;font-size:13px;display:flex;align-items:center;justify-content:center}
.card.dark .btn{top:301px}
.card.green .btn{top:325px;color:var(--green)}

/* services */
.services-title{top:1411px;width:1200px;text-align:center;font-family:Ubuntu,sans-serif;font-weight:500;font-size:26px;color:#222}
.services-title span{color:var(--green)}
.services-intro{top:1450px;width:1200px;text-align:center;font-size:14px;line-height:21px;color:#333}
.tabs{top:1529px;left:98px;width:1002px;height:185px;display:flex}
.tab{flex:1;background:var(--pale);border:1px solid #dfe5d6;padding:28px 37px;position:relative}
.tab h3{font-family:Ubuntu,sans-serif;font-weight:700;font-size:21px;color:var(--green);letter-spacing:.5px}
.tab .sub{font-style:italic;font-size:16.5px;color:#333;margin-top:2px}
.tab p{font-size:12.5px;line-height:18px;color:#444;margin-top:28px}
.tab.active{background:var(--green);border-color:var(--green)}
.tab.active h3,.tab.active .sub,.tab.active p{color:#fff}
.tab.active::after{content:"";position:absolute;left:160px;bottom:-22px;border:12px solid transparent;border-top:22px solid var(--green)}
.features{top:1768px;left:96px;width:1010px;display:grid;grid-template-columns:repeat(3,342px);row-gap:22px}
.feature svg{display:block;height:58px}
.feature h4{font-weight:400;font-size:16.5px;color:var(--green);margin-top:6px}
.feature p{font-size:10.5px;line-height:16.5px;color:#444;margin-top:7px;width:290px}

/* news */
.news{top:2133px;left:0;width:1200px;height:443px;background:var(--green);color:#fff;text-align:center}
.news h2{font-family:Ubuntu,sans-serif;font-weight:500;font-size:33px;margin-top:40px}
.news .intro-text{font-size:15.5px;line-height:21px;margin-top:12px}
.news-card{position:absolute;left:221px;top:155px;width:745px;height:220px;background:var(--pale);color:#444;padding:24px 22px}
.news-meta{font-size:11px}
.news-meta b{color:var(--green);font-weight:500}
.news-card h3{font-weight:400;font-size:16.5px;margin-top:8px;color:#333}
.news-card p{font-size:12px;line-height:21px;margin-top:8px}
.news-card .btn{display:inline-block;margin-top:14px;background:var(--green);color:#fff;font-size:11px;padding:10px 20px}

/* partners */
.partners{top:2576px;left:96px;width:1010px;height:89px;display:flex;justify-content:space-between;align-items:center}
.partners span{font-family:Ubuntu,sans-serif;font-weight:500;font-size:28px;color:#a7a7a7}

/* footer */
.footer .brand{left:98px;top:2692px}
.footer-links{top:2682px;left:362px;display:grid;grid-template-columns:88px 88px 88px;row-gap:6px;font-family:Poppins,sans-serif;font-size:13.5px;color:var(--green)}
.footer-contact{top:2682px;left:752px;font-family:Poppins,sans-serif;font-size:12.5px;line-height:19.5px;color:var(--green)}
.footer-address{top:2682px;left:953px;font-family:Poppins,sans-serif;font-size:12.5px;line-height:19.5px;color:var(--green)}
.bottombar{top:2777px;left:0;width:1200px;height:58px;background:var(--green);color:#fff;font-size:12px}
.bottombar .copy{position:absolute;left:98px;top:22px}
.bottombar svg{position:absolute;left:1058px;top:12px}
</style>
</head>
<body>

<header class="abs header">
  <div class="brand">
    <div class="brand-mark"></div>
    <div class="brand-name">Grünwerk</div>
  </div>
  <div class="phone">
    <svg width="18" height="18" viewBox="0 0 24 24"><path fill="#73a043" d="M6.6 10.8a15.1 15.1 0 0 0 6.6 6.6l2.2-2.2a1 1 0 0 1 1-.25 11.4 11.4 0 0 0 3.6.57 1 1 0 0 1 1 1V20a1 1 0 0 1-1 1A17 17 0 0 1 3 4a1 1 0 0 1 1-1h3.5a1 1 0 0 1 1 1c0 1.250.2 2.45.57 3.57a1 1 0 0 1-.25 1z"/></svg>
    +49 351/480 12 30
  </div>
  <div class="btn-contact">Kontakt</div>
</header>

<nav class="abs nav">
  <ul>
    <li class="active">Home</li><li>Leistungen</li><li>Beratung</li><li>Vertrieb</li><li>Recycling</li><li>Zertifikate</li><li>Vorstellung</li><li>Partner</li><li>Aktuelles</li>
  </ul>
</nav>

<section class="abs hero" role="img" aria-label="PIXANTO Foto: Windräder über einem Feld bei Sonnenuntergang">
  <svg class="hero-arrow" style="left:60px" width="30" height="54" viewBox="0 0 30 54"><path d="M28 2 3 27l25 25" fill="none" stroke="#fff" stroke-width="2"/></svg>
  <svg class="hero-arrow" style="left:1110px" width="30" height="54" viewBox="0 0 30 54"><path d="M2 2l25 25L2 52" fill="none" stroke="#fff" stroke-width="2"/></svg>
  <div class="hero-title">CORPORATE SUSTAINABILITY</div>
  <div class="hero-sub">WIR HELFEN IHNEN BEIM AUFBAU EINES UMWELTFREUNDLICHEN GESCHÄFTS.</div>
</section>

<section class="abs intro">
  <article class="card dark" style="left:99px;width:333px">
    <h2>Über uns</h2>
    <div class="lead">Grünwerk Vertriebsmanagement GmbH &amp; Co</div>
    <div class="body">
      <p>KG basiert auf langjähriger Erfahrung im Raffineriebetrieb, der Abfallwirtschaft und im Produkthandel.</p>
      <p>Für die Entsorgung Ihrer Abfälle und Reststoffe gemäß Verordnung über das Europäische Abfall­verzeichnis AVV bieten wir Ihnen als zertifizierter Entsorgungsfachbetrieb gemäß §2 EfbV alterna­tive kostengünstige Lösungen an.</p>
    </div>
    <div class="btn">WEITERLESEN</div>
  </article>
  <article class="card green" style="left:432px;width:333px">
    <h2>Vorstellung</h2>
    <div class="lead">Sed ut perspiciatis unde omnis iste natus</div>
    <div class="body"><p>Lorem ipsum dolor sit amet, consectetur adipi­scing elit, sed do eiusmod tempor incididunt ut labore et dolore magna aliqua. Ut enim ad minim veniam, quis nostrud exercitation ullamco labo­ris nisi ut aliquip ex ea commodo consequat. Duis aute irure dolor in reprehenderit in voluptate velit esse cillum dolore eu fugiat nulla pariatur.</p></div>
    <div class="btn">WEITERLESEN</div>
  </article>
  <article class="card dark" style="left:765px;width:333px">
    <h2>Zertifikate</h2>
    <div class="lead">Sed ut perspiciatis unde omnis iste natus</div>
    <div class="body"><p>Lorem ipsum dolor sit amet, consectetur adipi­scing elit, sed do eiusmod tempor incididunt ut labore et dolore magna aliqua. Ut enim ad minim veniam, quis nostrud exercitation ullamco labo­ris nisi ut aliquip ex ea commodo consequat. Duis aute irure dolor in reprehenderit in voluptate velit esse cillum dolore eu fugiat nulla pariatur.</p></div>
    <div class="btn">WEITERLESEN</div>
  </article>
</section>

<h2 class="abs services-title">Unsere Dienstleistungen und <span>Lösungen</span></h2>
<p class="abs services-intro">Wir bieten umfassende Beratungs, Vertriebs, Recycling, Qualitätskontroll- und<br>Nachhaltigkeitslösungen für Unternehmen und Konzerne.</p>

<div class="abs tabs">
  <div class="tab"><h3>BERATUNG</h3><div class="sub">Sed ut perspiciatis unde</div><p>Lorem ipsum dolor sit amet,<br>consectetur adipiscing elit, sed do<br>eiusmod tempor incididunt.</p></div>
  <div class="tab"><h3>VERTRIEB</h3><div class="sub">Sed ut perspiciatis unde</div><p>Lorem ipsum dolor sit amet,<br>consectetur adipiscing elit, sed do<br>eiusmod tempor incididunt.</p></div>
  <div class="tab active"><h3>RECYCLING</h3><div class="sub">Sed ut perspiciatis unde</div><p>Lorem ipsum dolor sit amet,<br>consectetur adipiscing elit, sed do<br>eiusmod tempor incididunt.</p></div>
</div>

<div class="abs features">
  <div class="feature">
    <svg viewBox="0 0 60 60" width="60"><g fill="none" stroke="#73a043" stroke-width="2"><path d="M22 14h16l-4 7H26z"/><path d="M26 21C12 28 8 52 20 55h20c12-3 8-27-6-34"/><circle cx="30" cy="40" r="8"/></g></svg>
    <h4>Müllsammlung</h4>
    <p>Lorem ipsum dolor sit amet, consectetur adipiscing elit, sed do eiusmod tempor incididunt ut labore et dolore magna aliqua.</p>
  </div>
  <div class="feature">
    <svg viewBox="0 0 60 60" width="60"><g fill="none" stroke="#73a043" stroke-width="2"><path d="M22 12h14l8 13M44 25l3-8M44 25l-8-1"/><path d="M48 36l-7 13H28M28 49l5 6M28 49l5-6"/><path d="M18 48 10 34l7-12M17 22l-8 1M17 22l2 8"/></g></svg>
    <h4>Recycling-Dienstleistungen</h4>
    <p>Lorem ipsum dolor sit amet, consectetur adipiscing elit, sed do eiusmod tempor incididunt ut labore et dolore magna aliqua.</p>
  </div>
  <div class="feature">
    <svg viewBox="0 0 60 60" width="60"><g fill="none" stroke="#73a043" stroke-width="2"><path d="M8 52c0-20 12-30 30-30 0 18-10 30-30 30zM8 52l22-22"/><circle cx="30" cy="8" r="4"/><circle cx="48" cy="42" r="4"/></g></svg>
    <h4>Umweltschutz</h4>
    <p>Lorem ipsum dolor sit amet, consectetur adipiscing elit, sed do eiusmod tempor incididunt ut labore et dolore magna aliqua.</p>
  </div>
  <div class="feature">
    <svg viewBox="0 0 60 60" width="60"><g fill="none" stroke="#73a043" stroke-width="2"><circle cx="30" cy="32" r="22"/><path d="M20 14c4 6 0 10 6 14s2 10 8 12M40 16c-4 6 4 10 10 8M36 50c0-6 6-8 10-6"/><path d="M6 14c4-6 10-8 14-6"/></g></svg>
    <h4>Qualitätsaudits</h4>
    <p>Lorem ipsum dolor sit amet, consectetur adipiscing elit, sed do eiusmod tempor incididunt ut labore et dolore magna aliqua.</p>
  </div>
  <div class="feature">
    <svg viewBox="0 0 60 60" width="60"><g fill="none" stroke="#73a043" stroke-width="2"><path d="M30 16c-6 8-8 12-8 16a8 8 0 0 0 16 0c0-4-2-8-8-16z"/><path d="M20 36c-4 5-5 7-5 10a5 5 0 0 0 10 0M40 36c4 5 5 7 5 10a5 5 0 0 1-10 0"/><path d="M10 26a22 22 0 0 1 40 0M50 26l2-7M50 26l-7-1"/></g></svg>
    <h4>BIOFuel-Produktion</h4>
    <p>Lorem ipsum dolor sit amet, consectetur adipiscing elit, sed do eiusmod tempor incididunt ut labore et dolore magna aliqua.</p>
  </div>
  <div class="feature">
    <svg viewBox="0 0 60 60" width="60"><g fill="none" stroke="#73a043" stroke-width="2"><path d="M30 40c-8-6-8-18 0-28 8 10 8 22 0 28zM30 40V20"/><path d="M4 22l4 20 12 12M56 22l-4 20-12 12"/><path d="M12 30l8 12M48 30l-8 12"/></g></svg>
    <h4>Nachhaltigkeit</h4>
    <p>Lorem ipsum dolor sit amet, consectetur adipiscing elit, sed do eiusmod tempor incididunt ut labore et dolore magna aliqua.</p>
  </div>
</div>

<section class="abs news">
  <h2>AKTUELL</h2>
  <p class="intro-text">Lorem ipsum dolor sit amet, consectetuer. Proin gravida nibh vel velit auctor aliquet. Aenean sollicitudin,<br>lorem quis bibendum auctor, nisi elit consequat ipsum, nec sagittis sem nibh id elit.</p>
  <article class="news-card">
    <div class="news-meta"><b>13. DEZEMBER 2016</b> &nbsp;|&nbsp; RECYCLING</div>
    <h3>Tipps zur Abfallentsorgung</h3>
    <p>Lorem ipsum dolor sit amet, consectetur adipiscing elit, sed do eiusmod tempor incididunt ut labore et dolore magna aliqua. Ut enim ad minim veniam, quis nostrud exercitation ullamco laboris nisi ut aliquip ex ea commodo consequat. Duis aute irure dolor in reprehenderit in voluptate velit esse cillum dolore eu fugiat nulla pariatur.</p>
    <span class="btn">WEITERLESEN</span>
  </article>
</section>

<div class="abs partners">
  <span>Norvalis</span><span>Kelvora</span><span>Trumeo</span><span>Plexa</span><span>Vandt</span>
</div>

<footer class="footer">
  <div class="brand">
    <div class="brand-mark"></div>
    <div class="brand-name">Grünwerk</div>
  </div>
  <div class="abs footer-links">
    <span>Home</span><span>Vertrieb</span><span>Vorstellung</span>
    <span>Leistungen</span><span>Recycling</span><span>Partner</span>
    <span>Beratung</span><span>Zertifikate</span><span>Aktuelles</span>
  </div>
  <div class="abs footer-contact">Fon: +49 351 - 480 12 30<br>Fax: +49 351 - 480 12 31<br>info(at)gruenwerk-beispiel.de</div>
  <div class="abs footer-address">Lindenallee 14<br>01067 Dresden</div>
</footer>

<div class="abs bottombar">
  <span class="copy">© Grünwerk Vertriebsmanagement GmbH &amp; Co.</span>
  <svg width="34" height="34" viewBox="0 0 34 34"><circle cx="17" cy="17" r="15" fill="none" stroke="#fff" stroke-width="2"/><path d="M10 20l7-7 7 7" fill="none" stroke="#fff" stroke-width="2"/></svg>
</div>

</body>
</html>
```